58 Restaurant & Bar Menu

Want to make current menu more trendy in design. I have attached a pdf of the menu and of the logo. Rather, than being 6 pages I would like to make the menu into "4 pages". The menu will be printed in color.

I am open to designs that will allow the menu to be printed on 11x17 paper that will be folded in half. The "Breakfast" section needs to be its own page and all the way on the back.

As for the cover I am open to just keeping it as a cover with the info I have on it but completely different design/picture change. The logo needs to stay. The cover can also be used as having menu items on there if pulled of correctly.

The readability has to be clear to the guests.

The restaurant is a Mediterranean style and for the area it is priced mid-high. The atmosphere is casual fine dining with Martini & Wine Bar. All are ingredients are fresh never frozen and everything is prepared from scratch.

Industry/Entity Type

Restaurant

Requirements
Must have
• Breakfast on its own page on the back.
Nice to have
• Trendy Design

```html
<!DOCTYPE html>
<html lang="en">
<head>
<meta charset="utf-8">
<title>58 Restaurant &amp; Bar — Start It Out</title>
<link rel="stylesheet" href="https://fonts.googleapis.com/css2?family=Oswald:wght@200;600&family=Fira+Sans+Condensed:ital,wght@0,500;0,600;0,700;1,600;1,700&family=Delius&display=swap">
<style>
  :root {
    --page-bg: #4b4e4d;
    --band: #f4f0c8;
    --accent: #a9e4e1;
    --text: #ffffff;
    --brand: #ffffff;
  }
  * { box-sizing: border-box; margin: 0; padding: 0; }
  html, body { width: 927px; height: 1200px; overflow: hidden; background: var(--page-bg); }
  .menu-page {
    position: relative;
    width: 927px;
    height: 1200px;
    overflow: hidden;
    background: var(--page-bg);
    font-family: "Fira Sans Condensed", "Arial Narrow", sans-serif;
    color: var(--text);
  }
  .brand {
    position: absolute;
    left: 56px;
    top: 255px;
    display: flex;
    align-items: center;
    gap: 18px;
  }
  .brand-dot {
    width: 46px; height: 46px;
    border-radius: 50%;
    background: var(--accent);
  }
  .brand-name {
    font-family: "Oswald", sans-serif;
    font-weight: 600;
    font-size: 60px;
    line-height: 1;
    letter-spacing: 1px;
    text-transform: uppercase;
    color: var(--brand);
  }
  .divider-band {
    position: absolute;
    left: 0; top: 364px;
    width: 927px; height: 12px;
    background: var(--band);
  }
  .section-title {
    position: absolute;
    left: 70px;
    top: 1090px;
    transform-origin: 0 0;
    transform: rotate(-90deg);
    font-family: "Oswald", sans-serif;
    font-weight: 200;
    font-size: 82px;
    line-height: 1;
    letter-spacing: 15px;
    color: var(--accent);
    white-space: nowrap;
  }
  .menu-column { position: absolute; top: 0; }
  .menu-column--starters { left: 323px; width: 215px; }
  .menu-column--salads { left: 592px; width: 228px; }
  .column-heading {
    position: absolute;
    top: 403px;
    font-family: "Delius", cursive;
    font-size: 20px;
    font-weight: 400;
    color: var(--accent);
    white-space: nowrap;
  }
  .menu-item { position: absolute; left: 0; width: 100%; }
  .item-head { display: flex; align-items: baseline; white-space: nowrap; }
  .item-name {
    font-style: italic;
    font-weight: 700;
    font-size: 12.5px;
    color: var(--accent);
  }
  .menu-column--starters .item-name { width: 162px; flex: none; }
  .menu-column--salads .item-name { width: 164px; flex: none; }
  .item-name small { font-size: 8px; text-transform: uppercase; letter-spacing: .3px; }
  .item-price { font-weight: 700; font-size: 16px; }
  .item-desc {
    font-weight: 600;
    font-size: 15.5px;
    line-height: 18px;
  }
  .soup-title {
    font-style: italic;
    font-weight: 700;
    font-size: 12.5px;
    color: var(--accent);
    text-decoration: underline;
  }
  .soup-row { display: flex; font-weight: 600; font-size: 15.5px; line-height: 20px; }
  .soup-row span:first-child { width: 162px; }
  .dressing-title { font-weight: 700; font-size: 13px; color: var(--accent); }
  .dressing-list { font-weight: 600; font-size: 11.5px; line-height: 16px; }
</style>
</head>
<body>
<main class="menu-page">
  <header class="brand">
    <span class="brand-dot" aria-hidden="true"></span>
    <span class="brand-name">58 Restaurant &amp; Bar</span>
  </header>
  <div class="divider-band"></div>

  <h1 class="section-title">START IT OUT</h1>

  <section class="menu-column menu-column--starters">
    <h2 class="column-heading">Meze (Starters)</h2>
    <div class="menu-item" style="top:440px">
      <div class="item-head"><span class="item-name">Calamari</span><span class="item-price">$8.95</span></div>
      <p class="item-desc">Fresh Calamari breaded with our house seasoned flour and served w/ chili lime sauce.</p>
    </div>
    <div class="menu-item" style="top:531px">
      <div class="item-head"><span class="item-name">Beer Battered Onion Rings</span><span class="item-price">$6.95</span></div>
      <p class="item-desc">Fresh sliced onion rings dipped in our beer batter and fried crisp.</p>
    </div>
    <div class="menu-item" style="top:604px">
      <div class="item-head"><span class="item-name">Mussels</span><span class="item-price">$10.95</span></div>
      <p class="item-desc">Fresh Mussels in a fire roasted tomato and garlic, Moscato wine sauce. Serve w/ char-grilled bread.</p>
    </div>
    <div class="menu-item" style="top:696px">
      <div class="item-head"><span class="item-name">Mozzarella Sticks</span><span class="item-price">$6.95</span></div>
      <p class="item-desc">Fresh mozzarella cheese wrapped with wontons and fried.</p>
    </div>
    <div class="menu-item" style="top:768px">
      <div class="item-head"><span class="item-name">Hummus Plate</span><span class="item-price">$8.95</span></div>
      <p class="item-desc">Spinach-feta hummus &amp; fire roasted tomato hummus served with an intense cucumber &amp; garlic dip, Mediterranean garnish and pita points.</p>
    </div>
    <div class="menu-item" style="top:895px">
      <div class="item-head"><span class="item-name">Saganaki</span><span class="item-price">$8.95</span></div>
      <p class="item-desc">Imported cheese dusted and fried in olive oil then flamed tableside with Ouzo.</p>
    </div>
    <div class="menu-item" style="top:987px">
      <p class="soup-title">Çorbë (Soup of the Day)</p>
      <p class="soup-row"><span>Cup</span><span>$2.95</span></p>
      <p class="soup-row"><span>Bowl</span><span>$3.95</span></p>
    </div>
  </section>

  <section class="menu-column menu-column--salads">
    <h2 class="column-heading">Salata (Salads)</h2>
    <div class="menu-item" style="top:440px">
      <div class="item-head"><span class="item-name">House</span><span class="item-price">$3.95</span></div>
      <p class="item-desc">Fresh Greens, fresh grapes &amp; candied walnuts w/ our lemon-mayo dressing.</p>
    </div>
    <div class="menu-item" style="top:531px">
      <div class="item-head"><span class="item-name">Greek</span><span class="item-price">$7.95</span></div>
      <p class="item-desc">Fresh Greens, Kalamata olives, imported feta, pepperchinis, onions, tomato, cucumbers, oregano. Served w/ Homemade Greek Dressing.</p>
    </div>
    <div class="menu-item" style="top:659px">
      <div class="item-head"><span class="item-name">Chicken Caesar</span><span class="item-price">$10.95</span></div>
      <p class="item-desc">Romaine lettuce, marinated chicken, croutons, imported parmesan. Served w/ Caesar Dressing.</p>
    </div>
    <div class="menu-item" style="top:768px">
      <div class="item-head"><span class="item-name">Grape Walnut</span><span class="item-price">$8.95</span></div>
      <p class="item-desc">Fresh Greens, Candied Walnuts, Grapes, Crumbled Bleu Cheese. Served w/ lemon-mayo Dressing.</p>
    </div>
    <div class="menu-item" style="top:860px">
      <div class="item-head"><span class="item-name">Shopska</span><span class="item-price">$7.95</span></div>
      <p class="item-desc">Cucumbers, tomatoes, onions, peppers, white brine cheese tossed in Vinaigrette.</p>
    </div>
    <div class="menu-item" style="top:951px">
      <div class="item-head"><span class="item-name">Salad <small>for the</small> Table</span><span class="item-price">$16.95</span></div>
      <p class="item-desc">Combination Platter of Greek Salad, Shopska Salad &amp; House Salad.</p>
    </div>
    <div class="menu-item" style="top:1039px">
      <p class="dressing-title">Dressing Choices:</p>
      <p class="dressing-list">Ranch, French, 1000 Island, Vinaigrette, Lemon-Mayo, Bleu Cheese</p>
    </div>
  </section>
</main>
</body>
</html>
```